GearVault.com

Our company, GearVault Inc., is an established business with an extensive worldwide customer base in the Aviation, Aerospace, and Defense Industries.
GearVault Inc, is an e-commerce platform driven by an aviation parts locator. We are looking to totally redo our homepage, log-in page, standard part search page, and results page.
Our current web design is in 800frame and we need it to be updated to a centered 1280 frame. The new design also needs to be easily viewed from any mobile device. The new size needs to accommodate 2-3 advertisements, both vertically and horizontally.
I like clean, simple, crisp lines that can easily be navigated by everyone. Along with Aviation/Aerospace stock photos, I would like to use different shades of blue and grey and accent specific buttons/drop-downs with orange or yellow.
We are also looking for a web designer who also has the ability to cut up the page and turn over to our .NET developers.
Attached are the 4 pages that I would like to start working on. The standard content within these pages need to be incorporated into the new design.
Our current website is www.gearvault.com
Below are some industry websites that I like the color and feel of.
Please use attached pic of skyreach T480 as main photo
http://www.corvanetrix.com/
http://www.talmoreaux.com/en/aerospace.html
http://www.qyparts.com/
http://aerospace.brindlecove.com/

```html
<!DOCTYPE html>
<html lang="en">
<head>
<meta charset="utf-8">
<title>GearVault.com – Aviation Parts</title>
<link rel="stylesheet" href="https://fonts.googleapis.com/css2?family=Open+Sans:ital,wght@0,400;0,600;0,700;1,400&display=swap">
<style>
:root{
  --blue:#0b7fd8;
  --navy:#1f2f9a;
  --sky:#1aa3dc;
  --orange:#f7891f;
  --grey:#9b9b9b;
  --panel:#efefef;
  --text:#333;
  --foot:#4a4a4a;
  --foot-line:#5f5f5f;
}
*{box-sizing:border-box;margin:0;padding:0}
html,body{width:724px;height:1200px;overflow:hidden}
body{position:relative;background:#fff;font-family:"Open Sans",Arial,sans-serif;color:var(--text)}
.abs{position:absolute}
.topline{left:0;top:0;width:724px;height:2px;background:var(--blue)}
.brand{left:104px;top:24px;font-size:18px;font-weight:700;color:var(--blue);display:flex;align-items:center;gap:5px;letter-spacing:.2px}
.brand .mark{width:9px;height:9px;background:var(--blue)}
.search{left:437px;top:18px;width:65px;height:8px;border:1px solid #ccc;font-size:5px;color:#999;padding-left:3px;line-height:7px}
.cart{left:509px;top:18px;width:53px;height:8px;background:var(--blue);color:#fff;font-size:5px;line-height:8px;padding-left:4px}
.sign{top:18px;height:8px;background:var(--grey);color:#fff;font-size:5px;line-height:8px;text-align:center}
.toplinks{top:41px;font-size:7.5px;color:#222;letter-spacing:.2px}
.toplinks.active{color:var(--navy)}
.mainnav{left:104px;top:68px;width:515px;height:20px;background:var(--navy);display:flex;justify-content:space-around;align-items:center;padding:0 6px}
.mainnav span{color:#fff;font-size:7px;letter-spacing:.2px;position:relative}
.mainnav span.on::after{content:"";position:absolute;left:50%;bottom:-6px;margin-left:-3px;border:3px solid transparent;border-bottom-color:#fff}
.hero{left:0;top:78px;width:724px;height:265px;
  background:
    radial-gradient(ellipse 260px 60px at 560px 150px,rgba(255,214,140,.75),rgba(255,214,140,0) 70%),
    radial-gradient(ellipse 300px 40px at 180px 60px,rgba(70,70,80,.55),rgba(70,70,80,0) 70%),
    radial-gradient(ellipse 200px 50px at 300px 150px,rgba(205,210,215,.55),rgba(205,210,215,0) 70%),
    linear-gradient(180deg,#5f6068 0%,#8f8272 22%,#c8a470 40%,#e0b87c 50%,#8b8a55 56%,#6b6e3f 62%,#75766a 72%,#5b5a52 88%,#3f3e38 100%)}
.caption{left:448px;top:179px;width:154px;height:43px;background:rgba(40,38,34,.85);color:#fff;font-size:11px;line-height:13px;padding:9px 14px;letter-spacing:.3px}
.caption-go{left:602px;top:179px;width:17px;height:43px;background:var(--orange)}
.heading{left:0;width:724px;top:366px;text-align:center;font-size:12px;letter-spacing:.4px;color:#222;font-weight:400}
.viewall{font-size:4.8px;color:var(--orange);text-decoration:underline}
.products{left:104px;top:398px;width:515px;height:150px;background:var(--panel);border:1px solid #ddd}
.card{top:412px;width:112px}
.card .pic{height:87px}
.card .price{position:absolute;left:0;top:0;background:#fff;font-size:11px;padding:2px 6px;color:#222}
.card .title{text-align:center;font-size:7px;margin-top:7px;color:#333}
.card .btns{display:flex;justify-content:center;gap:3px;margin-top:5px}
.card .btn{height:9px;font-size:4.8px;color:#fff;background:var(--grey);line-height:9px;padding:0 5px}
.card.hot .btn{background:var(--orange)}
.tabs{top:578px;height:20px;display:flex}
.tab{height:20px;font-size:6px;line-height:20px;text-align:center;background:#e9e9e9;color:#555;border-right:1px solid #fff}
.tab.on{background:var(--blue);color:#fff;font-weight:600}
.newsbar{left:104px;top:598px;width:373px;height:3px;background:var(--blue)}
.newsbox{left:104px;top:601px;width:373px;height:141px;border:1px solid #e3e3e3;border-top:0}
.item{width:166px;height:34px;display:flex;gap:5px}
.item .thumb{width:39px;height:27px;flex:none}
.item p{font-size:4.4px;line-height:7px;color:#666}
.item b{display:block;color:#333;font-weight:700}
.item i{color:#999}
.rule{height:0;border-top:1px dashed #ccc}
.solbox{left:104px;top:761px;width:373px;height:185px;border:1px solid #e3e3e3}
.soltab{top:766px;height:16px;font-size:7px;line-height:16px;text-align:center;background:#e6e6e6;color:#777}
.soltab.on{background:var(--blue);color:#fff}
.soltab.on::after{content:"";position:absolute;left:50%;bottom:-4px;margin-left:-3px;border:3px solid transparent;border-top-color:var(--blue);border-bottom:0}
.sol-h{left:284px;top:803px;font-size:12px;font-weight:700;color:var(--blue)}
.sol-p{left:284px;top:824px;width:180px;font-size:6.3px;line-height:7.7px;color:#333}
.sol-link{left:284px;width:183px;font-size:6.3px;color:var(--orange);border-bottom:1px solid #eee;padding-bottom:3px}
.ad{left:498px;width:121px}
.ad-head{height:20px;background:var(--sky);color:#fff;font-size:8px;line-height:20px;padding-left:11px}
.ad-cap{position:absolute;left:7px;bottom:7px;font-size:6.3px;line-height:8px;color:#fff;width:100px}
.footer{left:0;top:985px;width:724px;height:215px;background:var(--foot)}
.f-h{top:1018px;font-size:9.5px;color:#eee;padding-bottom:5px;border-bottom:1px solid var(--foot-line);font-weight:400}
.f-p{font-size:6.3px;line-height:7.8px;color:#e5e5e5;font-weight:400}
.click{left:104px;top:1097px;width:31px;height:7px;border-radius:4px;background:var(--orange);color:#fff;font-size:3.8px;line-height:7px;text-align:center}
.f-rule{left:0;width:724px;height:1px;background:var(--foot-line)}
.f-links{top:1138px;left:104px;display:flex;gap:10px;font-size:5.4px;color:#eee}
.copy{top:1180px;font-size:5.4px;color:#ddd}
</style>
</head>
<body>
<div class="abs topline"></div>

<header>
  <div class="abs brand"><span class="mark"></span>GearVault</div>
  <div class="abs search">Search</div>
  <div class="abs cart">MY CART &nbsp; 01</div>
  <div class="abs sign" style="left:566px;width:26px">SIGNIN</div>
  <div class="abs sign" style="left:593px;width:26px">SIGNUP</div>
  <div class="abs toplinks active" style="left:414px">GEARVAULT MAIN</div>
  <div class="abs toplinks" style="left:494px">AERO PAGES</div>
  <div class="abs toplinks" style="left:554px">MESSAGE BOARD</div>
</header>

<div class="abs hero" role="img" aria-label="Business jet parked on a runway at sunset"></div>
<nav class="abs mainnav">
  <span>HOME</span><span class="on">ABOUT US</span><span>MEMBERSHIP</span><span>BUYERS SUPPLIERS</span><span>GOVERNMENT DATA</span><span>ADVERTISE</span><span>MEDIA</span><span>FAQS</span><span>CONTACT</span>
</nav>
<div class="abs caption">lorem ipsum dolor sit<br>amet consec tetur</div>
<svg class="abs caption-go" viewBox="0 0 17 43"><path d="M7 18l4 3.5-4 3.5" fill="none" stroke="#fff" stroke-width="1.8"/></svg>
<svg class="abs" style="left:559px;top:288px" width="60" height="22" viewBox="0 0 60 22">
  <circle cx="11" cy="11" r="9.5" fill="none" stroke="#ddd" stroke-width="1.2"/><path d="M13 7l-4 4 4 4" fill="none" stroke="#ddd" stroke-width="1.3"/>
  <circle cx="49" cy="11" r="9.5" fill="none" stroke="#ddd" stroke-width="1.2"/><path d="M47 7l4 4-4 4" fill="none" stroke="#ddd" stroke-width="1.3"/>
</svg>

<h2 class="abs heading">Shop Aviation Parts</h2>
<div class="abs viewall" style="left:582px;top:374px">Click to View All</div>

<section class="abs products"></section>
<div class="abs card hot" style="left:116px"><div class="pic" role="img" aria-label="Jet engine intake close-up" style="background:radial-gradient(circle at 38% 62%,#2b2a28 0 20%,#8c8a86 34%,#4a4844 48%,rgba(74,72,68,0) 62%),linear-gradient(135deg,#6b6650,#d8b45a 55%,#3a3834)"></div><div class="price">$799</div><div class="title">Lorem Ipsum Title</div><div class="btns"><span class="btn">Add to Cart</span><span class="btn">More Detail +</span></div></div>
<div class="abs card" style="left:242px"><div class="pic" role="img" aria-label="Cockpit control panel" style="background:radial-gradient(circle at 48% 22%,rgba(120,220,90,.8),rgba(120,220,90,0) 14%),radial-gradient(ellipse at 30% 70%,#6f8a94,rgba(111,138,148,0) 50%),linear-gradient(135deg,#3a4a50,#8a9ea3 50%,#232b2e)"></div><div class="price">$999</div><div class="title">Lorem Ipsum Title</div><div class="btns"><span class="btn">Add to Cart</span><span class="btn">More Detail +</span></div></div>
<div class="abs card" style="left:369px"><div class="pic" role="img" aria-label="Metal gears and machine parts" style="background:radial-gradient(circle at 40% 40%,#d3e9f3,rgba(211,233,243,0) 35%),radial-gradient(circle at 75% 70%,#1b5a80,rgba(27,90,128,0) 45%),linear-gradient(135deg,#2a88b8,#7fbcd8 50%,#1d5f86)"></div><div class="price">$559</div><div class="title">Lorem Ipsum Title</div><div class="btns"><span class="btn">Add to Cart</span><span class="btn">More Detail +</span></div></div>
<div class="abs card" style="left:495px"><div class="pic" role="img" aria-label="Passenger jet in flight against blue sky" style="background:radial-gradient(ellipse 40px 22px at 45% 60%,#3d4550,rgba(61,69,80,0) 70%),radial-gradient(ellipse at 80% 85%,#e6eef6,rgba(230,238,246,0) 45%),linear-gradient(180deg,#4f86c4,#a9c8e6)"></div><div class="price">$859</div><div class="title">Lorem Ipsum Title</div><div class="btns"><span class="btn">Add to Cart</span><span class="btn">More Detail +</span></div></div>

<div class="abs tabs" style="left:104px">
  <div class="tab on" style="width:70px">Latest News</div>
  <div class="tab" style="width:70px">Latest Blog</div>
  <div class="tab" style="width:76px">Upcoming Events</div>
</div>
<div class="abs viewall" style="left:424px;top:585px">Click to View All News</div>
<div class="abs newsbar"></div>
<section class="abs newsbox"></section>
<div class="abs" style="left:293px;top:608px;width:1px;height:118px;background:#e3e3e3"></div>

<div class="abs item" style="left:120px;top:611px"><div class="thumb" role="img" aria-label="Technician at work" style="background:linear-gradient(135deg,#c9b49a,#6e5a48)"></div><p><b>Lorem ipsum dolor sit amet</b>Consectetur adipiscing sed do eiusmod tempor<br>incidi dunt labore et dolore magna aliqua adip<br><i>Learn More - 03 Aug 2014</i></p></div>
<div class="abs item" style="left:302px;top:611px"><div class="thumb" role="img" aria-label="Pilot in cockpit" style="background:linear-gradient(135deg,#9fb6c8,#4d6680)"></div><p><b>Lorem ipsum dolor sit amet</b>Consectetur adipiscing sed do eiusmod tempor<br>incidi dunt labore et dolore magna aliqua adip<br><i>Learn More - 03 Aug 2014</i></p></div>
<div class="abs rule" style="left:120px;top:646px;width:160px"></div><div class="abs rule" style="left:302px;top:646px;width:164px"></div>
<div class="abs item" style="left:120px;top:652px"><div class="thumb" role="img" aria-label="Engineer with equipment" style="background:linear-gradient(135deg,#6c98c4,#25466e)"></div><p><b>Lorem ipsum dolor sit amet</b>Consectetur adipiscing sed do eiusmod tempor<br>incidi dunt labore et dolore magna aliqua adip<br><i>Learn More - 03 Aug 2014</i></p></div>
<div class="abs item" style="left:302px;top:652px"><div class="thumb" role="img" aria-label="Aircraft engine detail" style="background:linear-gradient(135deg,#1d2b55,#5b78b8 60%,#1a2240)"></div><p><b>Lorem ipsum dolor sit amet</b>Consectetur adipiscing sed do eiusmod tempor<br>incidi dunt labore et dolore magna aliqua adip<br><i>Learn More - 03 Aug 2014</i></p></div>
<div class="abs rule" style="left:120px;top:688px;width:160px"></div><div class="abs rule" style="left:302px;top:688px;width:164px"></div>
<div class="abs item" style="left:120px;top:694px"><div class="thumb" role="img" aria-label="Ground crew beside aircraft" style="background:linear-gradient(135deg,#d9c9b8,#c0573a 55%,#6a4a3a)"></div><p><b>Lorem ipsum dolor sit amet</b>Consectetur adipiscing sed do eiusmod tempor<br>incidi dunt labore et dolore magna aliqua adip<br><i>Learn More - 03 Aug 2014</i></p></div>
<div class="abs item" style="left:302px;top:694px"><div class="thumb" role="img" aria-label="Turbine blades" style="background:radial-gradient(circle at 50% 50%,#8a8a90,#3a3a3f 70%)"></div><p><b>Lorem ipsum dolor sit amet</b>Consectetur adipiscing sed do eiusmod tempor<br>incidi dunt labore et dolore magna aliqua adip<br><i>Learn More - 03 Aug 2014</i></p></div>

<section class="abs solbox"></section>
<div class="abs soltab on" style="left:110px;width:56px">Solutions</div>
<div class="abs soltab" style="left:168px;width:88px">Our Community</div>
<div class="abs soltab" style="left:258px;width:108px">Industry Connections</div>
<div class="abs soltab" style="left:367px;width:104px">Member Advantage</div>
<div class="abs" role="img" aria-label="Aviation mechanic in a hangar" style="left:114px;top:799px;width:160px;height:124px;background:radial-gradient(ellipse 60px 50px at 35% 80%,#2f7fd0,rgba(47,127,208,0) 70%),radial-gradient(ellipse at 80% 40%,#9a8a6e,rgba(154,138,110,0) 55%),linear-gradient(135deg,#d8dde4,#8da2b8 45%,#3c4a5c)"></div>
<h3 class="abs sol-h">Solutions</h3>
<p class="abs sol-p">Lorem ipsum dolor sit amet, consectetur adipisicing elit, sed do eiusmod tempor incidi dunt ut labore lorem ipsum dolor sit amet, consectetur adipisicing elit, sed do tempor incidi dunt ut labore lorem ipsum dolor sitLorem ipsum dolor sit amet, consectetur adipisicing elit,</p>
<div class="abs sol-link" style="top:874px">Buyer Solutions</div>
<div class="abs sol-link" style="top:889px">Government Data</div>
<div class="abs sol-link" style="top:903px">Supplier Solutions</div>

<aside>
  <div class="abs ad" role="img" aria-label="Advertisement: free stock images, pixelcrate.com" style="top:583px;height:101px;background:radial-gradient(ellipse 30px 30px at 60px 25px,#e6c9a0,rgba(230,201,160,0) 70%),linear-gradient(180deg,#d2d2d2,#a9a9a9)">
    <div style="position:absolute;left:36px;top:46px;width:58px;height:36px;background:#fff"></div>
    <div style="position:absolute;left:0;width:121px;top:48px;text-align:center;font-size:7.5px;line-height:9px;color:#333">Stock Images<br>for FREE</div>
    <div style="position:absolute;left:37px;top:72px;width:47px;height:9px;background:#3aa53a;color:#fff;font-size:4.8px;line-height:9px;text-align:center">Download now</div>
    <div style="position:absolute;right:5px;bottom:5px;font-size:6.3px;color:#333;font-weight:700">pixelcrate.com</div>
  </div>
  <div class="abs ad" style="top:698px;height:121px">
    <div class="ad-head">Customer Service</div>
    <div role="img" aria-label="Engineer in hard hat on the phone beside an engine" style="height:101px;position:relative;background:radial-gradient(circle at 80% 55%,#c7ced8,rgba(199,206,216,0) 40%),radial-gradient(ellipse 40px 50px at 25% 70%,#d43a32,rgba(212,58,50,0) 75%),linear-gradient(135deg,#2a2f3a,#3b4a62 60%,#8594a8)"><div class="ad-cap">Lorem ipsum dolor sit amet, elit sed do eiusmod</div></div>
  </div>
  <div class="abs ad" style="top:827px;height:121px">
    <div class="ad-head">Buyer Service</div>
    <div role="img" aria-label="Worker in hard hat inspecting machinery" style="height:101px;position:relative;background:radial-gradient(circle at 20% 45%,#e3b12a,rgba(227,177,42,0) 18%),radial-gradient(ellipse at 70% 40%,#eef2f5,rgba(238,242,245,0) 45%),linear-gradient(135deg,#4a5560,#a9b5bf 50%,#3c444c)"><div class="ad-cap">Lorem ipsum dolor sit amet, elit sed do eiusmod</div></div>
  </div>
</aside>

<footer class="abs footer"></footer>
<h4 class="abs f-h" style="left:104px;width:190px">About us</h4>
<p class="abs f-p" style="left:104px;top:1043px;width:195px">Lorem ipsum dolor sit amet, consectetur adipisicing elit, sed do eiusmod tempor incidi dunt ut labore lorem ipsum dolor sit amet, consectetur adipisicing elit, sed do tempor incidi dunt ut labore lorem ipsum dolor sitLorem ipsum dolor sit amet, consectetur adipisicing elit, sed do eiusmod tempor incidi dunt ut labore lorem</p>
<div class="abs click">CLICK HERE</div>
<h4 class="abs f-h" style="left:346px;width:96px">Social Share</h4>
<svg class="abs" style="left:346px;top:1042px" width="96" height="24" viewBox="0 0 96 24" role="img" aria-label="Share buttons">
  <g fill="none" stroke="#eee" stroke-width="1.2">
    <circle cx="12" cy="12" r="10.5"/><circle cx="36" cy="12" r="10.5"/><circle cx="60" cy="12" r="10.5"/><circle cx="84" cy="12" r="10.5"/>
  </g>
  <g fill="#eee">
    <circle cx="12" cy="12" r="2.2"/><circle cx="36" cy="12" r="2.2"/><circle cx="60" cy="12" r="2.2"/><circle cx="84" cy="12" r="2.2"/>
  </g>
</svg>
<h4 class="abs f-h" style="left:482px;width:137px">Testimonials</h4>
<p class="abs f-p" style="left:482px;top:1043px;width:137px;line-height:13px">We had an AOG issue last night. I logged into GearVault.com and had the part ordered in about five minutes.</p>
<div class="abs f-p" style="left:482px;top:1088px;color:var(--sky);font-style:italic">Dale Harwick, Fenmore Industries, Inc</div>
<div class="abs f-p" style="left:481px;top:1104px;font-style:italic">More Testimonials</div>
<div class="abs f-rule" style="top:1126px"></div>
<nav class="abs f-links"><span>Home</span><span>About Us</span><span>Membership</span><span>Buyers Suppliers</span><span>Government Data</span><span>Advertise</span><span>Media</span><span>Faqs</span><span>Contact</span></nav>
<div class="abs f-rule" style="top:1158px"></div>
<div class="abs copy" style="left:104px">Copyright© 2014 GearVault.com. All rights reserved.</div>
<div class="abs copy" style="left:455px">About gearvault.com &nbsp;·&nbsp; Terms &nbsp;·&nbsp; Disclaimer &nbsp;·&nbsp; Privacy Policy</div>
</body>
</html>
```